Website for IT consulting Company

I need a website upgrade, the existing site content is ok, I would also like to add a testimonial page, the site should be something that is easy for us to update content. You use the content from www.kavnex.com as an example. I will also post update logo and artwork. I also need a contact form with some type of validation or captcha.

I added Coded to the Project

Please omit Address maps

Target Market(s)

small business, service oriented companies. We provide IT Consulting, support and mangement

Industry/Entity Type

Information Technology

Coding

Coded - Design and coding required

Number of Pages Required

1 page

Font styles to use
Serif
Sans Serif

Requirements
Must have
• Contain logo attached, and content from existing web site www.kavnex.com.
• Also need to update content easily, and be movable to different platforms.
• There is a catch phrase
• "Let us worry about your technology…” “ so you don’t have to!”
• Should be included.
Nice to have
• Testimonial page, Project page where we can post new and past projects and pictures
Should not have
• none

```html
<!DOCTYPE html>
<html lang="en">
<head>
<meta charset="utf-8">
<title>Kavnex – IT Solutions</title>
<link href="https://fonts.googleapis.com/css2?family=Open+Sans:wght@400;600;700;800&display=swap" rel="stylesheet">
<style>
:root{
  --orange:#f47a20;
  --orange-dark:#e06a12;
  --ink:#333333;
  --muted:#666666;
  --dark:#1c1c1c;
  --nav:#232323;
  --light:#f2f2f2;
  --white:#ffffff;
  --line:#dddddd;
}
*{box-sizing:border-box;margin:0;padding:0}
html,body{width:1200px;height:3502px;overflow:hidden}
body{font-family:"Open Sans",Arial,sans-serif;color:var(--ink);background:var(--white);position:relative}

/* top bar */
.topbar{position:absolute;left:0;top:0;width:1200px;height:105px;background:var(--dark)}
.catch{position:absolute;left:65px;top:22px;color:var(--orange);font-weight:800;font-size:30px;letter-spacing:.3px}
.catch-sub{position:absolute;left:65px;top:70px;color:var(--white);font-weight:700;font-size:13px}
.social-top{position:absolute;left:928px;top:32px;display:flex;gap:6px}
.social-top span,.social-foot span{display:block;width:22px;height:22px;background:#444;border:1px solid #666}
.search{position:absolute;left:1120px;top:34px}

/* nav */
.navbar{position:absolute;left:0;top:105px;width:1200px;height:112px;background:var(--nav)}
.brand{position:absolute;left:65px;top:30px;display:flex;align-items:center;gap:12px}
.brand-mark{width:44px;height:44px;background:var(--orange)}
.brand-name{font-weight:800;font-size:40px;color:var(--white);letter-spacing:1px}
.menu{position:absolute;top:40px;left:0;width:1200px;height:36px}
.menu a{position:absolute;top:0;height:36px;line-height:36px;color:var(--white);font-size:14px;font-weight:600;text-decoration:none;padding:0 12px}
.menu a.active{background:var(--orange)}

/* hero */
.hero{position:absolute;left:0;top:217px;width:1200px;height:469px;background:linear-gradient(100deg,#5d6670 0%,#b9bec4 40%,#e6e8ea 70%,#9aa6b2 100%)}
.hero-title{position:absolute;left:65px;top:140px;width:560px;color:var(--white);font-size:36px;font-weight:600;line-height:44px}
.hero-sub{position:absolute;left:65px;top:230px;color:var(--white);font-size:15px;font-weight:600}
.btn{display:inline-block;background:var(--orange);color:var(--white);font-weight:700;font-size:13px;text-align:center}
.hero .btn{position:absolute;left:65px;top:283px;width:104px;height:35px;line-height:35px;border-radius:3px}
.arrow{position:absolute;top:200px;width:34px;height:34px;background:var(--orange)}
.dots{position:absolute;left:566px;top:415px;display:flex;gap:12px}
.dots span{width:18px;height:18px;border-radius:50%;background:var(--white)}
.dots span.on{background:var(--orange)}

/* support */
.support{position:absolute;left:0;top:686px;width:1200px;height:559px;background:var(--light)}
.section-title{text-align:center;font-size:35px;font-weight:600;color:var(--ink)}
.support .section-title{position:absolute;top:62px;width:1200px}
.support .lead{position:absolute;top:122px;left:280px;width:640px;text-align:center;font-size:14px;line-height:24px;color:var(--ink)}
.service{position:absolute;width:330px;height:110px}
.service .ring{position:absolute;left:0;top:0;width:104px;height:104px;border-radius:50%;background:var(--white);border:1px solid #e2e2e2;display:flex;align-items:center;justify-content:center}
.service h3{position:absolute;left:126px;top:8px;font-size:14px;font-weight:600;color:var(--ink)}
.service p{position:absolute;left:126px;top:38px;width:200px;font-size:14px;line-height:23px;color:var(--muted)}

/* solutions */
.solutions{position:absolute;left:0;top:1245px;width:1200px;height:1060px;background:linear-gradient(180deg,#2a2a2a 0%,#3a3734 55%,#2c2926 100%)}
.solutions .section-title{position:absolute;top:60px;width:1200px;color:var(--white);font-size:37px}
.solutions .intro{position:absolute;left:60px;top:126px;width:1080px;text-align:center;color:var(--white);font-size:14px;line-height:23px}
.card{position:absolute;width:337px;height:330px;background:var(--white)}
.card .art{position:absolute;left:26px;top:36px;width:68px;height:68px;border-radius:50%}
.card h4{position:absolute;left:120px;top:44px;width:150px;font-size:18px;font-weight:400;line-height:22px;color:#555}
.card h4.mid{width:185px}
.card p{position:absolute;left:120px;top:108px;width:190px;font-size:12.5px;line-height:21px;color:#444}
.card.short p{top:80px}

/* contact */
.contact{position:absolute;left:0;top:2305px;width:1200px;height:450px;background:var(--light)}
.col-title{font-size:20px;font-weight:600;color:var(--ink);padding-bottom:14px;border-bottom:1px solid var(--line)}
.qc{position:absolute;left:65px;top:88px;width:520px}
.field{display:block;width:493px;height:40px;margin-top:13px;background:var(--white);border:1px solid #d8d8d8;font-size:12px;color:#999;padding:12px 14px}
.field.area{height:73px}
.qc .btn{position:absolute;left:0;top:262px;width:188px;height:33px;line-height:33px;font-size:19px}
.why{position:absolute;left:614px;top:88px;width:520px}
.why p{margin-top:24px;font-size:14px;line-height:25px;color:var(--ink)}

/* tabs & testimonials */
.tabs{position:absolute;left:65px;top:2818px;width:703px;height:304px;border:1px solid #e0e0e0;background:var(--white)}
.tab-list{position:absolute;left:0;top:0;width:175px}
.tab-list div{height:48px;line-height:48px;padding-left:16px;font-size:12.5px;color:#555;background:#f1f1f1;border-bottom:1px solid #e2e2e2}
.tab-list div.on{background:#222;color:var(--white);width:192px;clip-path:polygon(0 0,92% 0,100% 50%,92% 100%,0 100%)}
.tab-photo{position:absolute;left:212px;top:20px;width:196px;height:178px;background:linear-gradient(135deg,#c9a98a,#7d6a5a 60%,#a89e94)}
.tab-body{position:absolute;left:424px;top:18px;width:250px}
.tab-body h5{font-size:15px;font-weight:600;color:#333}
.tab-body p{margin-top:10px;font-size:12.5px;line-height:21px;color:#444}
.testimonials{position:absolute;left:798px;top:2812px;width:340px}
.testimonials h6{font-size:15px;font-weight:600;color:#333}
.quote{margin-top:18px;border-left:1px solid #ccc;padding-left:34px;font-size:12.5px;line-height:21px;color:#444}
.quote b{display:block;margin-top:8px;font-size:12.5px}

/* footer */
.footer{position:absolute;left:0;top:3145px;width:1200px;height:275px;background:#efefef}
.fcol{position:absolute;top:70px}
.fcol h6{font-size:20px;font-weight:400;color:#222;letter-spacing:.5px}
.fcol p{font-size:12.5px;line-height:28px;color:#333;margin-top:22px}
.news-field{margin-top:22px;width:156px;height:40px;background:var(--white);border:1px solid #d5d5d5;font-size:12px;color:#999;padding:12px 10px}
.fcol .btn{margin-top:8px;width:84px;height:33px;line-height:33px;font-size:18px}
.social-foot{display:flex;gap:6px;margin-top:26px}
.social-foot span{background:#333;border-color:#333}
.rule{position:absolute;left:0;top:3420px;width:1200px;height:4px;background:var(--orange)}
.bottom{position:absolute;left:0;top:3424px;width:1200px;height:78px;background:#1c1c1c;color:var(--white);font-size:13px}
.bottom .copy{position:absolute;left:65px;top:30px}
.bottom .links{position:absolute;right:65px;top:30px;display:flex;gap:24px}
</style>
</head>
<body>

<header class="topbar">
  <div class="catch">LET US WORRY ABOUT YOUR TECHNOLOGY...</div>
  <div class="catch-sub">SO YOU DON'T HAVE TO!</div>
  <div class="social-top"><span></span><span></span><span></span><span></span><span></span></div>
  <svg class="search" width="16" height="16" viewBox="0 0 16 16"><circle cx="6.5" cy="6.5" r="4.5" fill="none" stroke="#fff" stroke-width="2"/><line x1="10" y1="10" x2="14" y2="14" stroke="#fff" stroke-width="2"/></svg>
</header>

<nav class="navbar">
  <div class="brand"><span class="brand-mark"></span><span class="brand-name">KAVNEX</span></div>
  <div class="menu">
    <a class="active" style="left:553px">Home</a>
    <a style="left:670px">About Us</a>
    <a style="left:776px">Support</a>
    <a style="left:876px">Clients</a>
    <a style="left:974px">Careers</a>
    <a style="left:1075px">Contact</a>
  </div>
</nav>

<section class="hero" role="img" aria-label="Hand touching glowing technology cubes">
  <h1 class="hero-title">IT solutions that work for your business</h1>
  <div class="hero-sub">A full service technology company</div>
  <span class="btn">Read More</span>
  <svg class="arrow" style="left:12px" viewBox="0 0 34 34"><rect width="34" height="34" fill="#f47a20"/><path d="M20 10 L13 17 L20 24" fill="none" stroke="#fff" stroke-width="3"/></svg>
  <svg class="arrow" style="left:1154px" viewBox="0 0 34 34"><rect width="34" height="34" fill="#f47a20"/><path d="M14 10 L21 17 L14 24" fill="none" stroke="#fff" stroke-width="3"/></svg>
  <div class="dots"><span></span><span class="on"></span></div>
</section>

<section class="support">
  <h2 class="section-title">IT Support Solutions</h2>
  <p class="lead">Lorem ipsum dolor sit amet, consectetur adipisicing elit, sed do eiusmod tempor incididunt ut et dolore magna aliqua. Ut enim ad minim veniam</p>

  <div class="service" style="left:70px;top:242px">
    <div class="ring"><svg width="40" height="40" viewBox="0 0 40 40"><path d="M6 16h6l16-8v24l-16-8H6z" fill="#f47a20"/><rect x="10" y="24" width="5" height="9" fill="#f47a20"/></svg></div>
    <h3>NETWORK ADMINISTRATION</h3><p>Lorem ipsum dolor sit amet, consectetur adipisicing elit</p>
  </div>
  <div class="service" style="left:436px;top:242px">
    <div class="ring"><svg width="40" height="40" viewBox="0 0 40 40"><ellipse cx="20" cy="18" rx="15" ry="12" fill="#f47a20"/><path d="M10 26 L8 34 L17 28z" fill="#f47a20"/><circle cx="14" cy="18" r="2" fill="#fff"/><circle cx="20" cy="18" r="2" fill="#fff"/><circle cx="26" cy="18" r="2" fill="#fff"/></svg></div>
    <h3>DESKTOP SUPPORT</h3><p>Lorem ipsum dolor sit amet, consectetur adipisicing elit</p>
  </div>
  <div class="service" style="left:801px;top:242px">
    <div class="ring"><svg width="40" height="40" viewBox="0 0 40 40"><path d="M11 30a8 8 0 0 1 0-16a10 10 0 0 1 19 2a7 7 0 0 1 0 14z" fill="#f47a20"/><path d="M20 15v10M15 21l5 5l5-5" fill="none" stroke="#fff" stroke-width="2.5"/></svg></div>
    <h3>NETWORK CABLING</h3><p>Lorem ipsum dolor sit amet, consectetur adipisicing elit</p>
  </div>
  <div class="service" style="left:70px;top:384px">
    <div class="ring"><svg width="40" height="40" viewBox="0 0 40 40"><path d="M8 32C8 16 18 8 34 8C34 24 26 32 12 30z" fill="#f47a20"/><path d="M8 32L24 16" stroke="#fff" stroke-width="2"/></svg></div>
    <h3>WIRELESS NETWORKS</h3><p>Lorem ipsum dolor sit amet, consectetur adipisicing elit</p>
  </div>
  <div class="service" style="left:436px;top:384px">
    <div class="ring"><svg width="40" height="40" viewBox="0 0 40 40"><circle cx="15" cy="22" r="8" fill="none" stroke="#f47a20" stroke-width="5" stroke-dasharray="4 2.3"/><circle cx="29" cy="12" r="5" fill="none" stroke="#f47a20" stroke-width="4" stroke-dasharray="3 1.7"/></svg></div>
    <h3>ANTIVIRUS SOLUTIONS</h3><p>Lorem ipsum dolor sit amet, consectetur adipisicing elit</p>
  </div>
  <div class="service" style="left:801px;top:384px">
    <div class="ring"><svg width="40" height="40" viewBox="0 0 40 40"><path d="M20 34L6 20a8 8 0 0 1 14-10a8 8 0 0 1 14 10z" fill="#f47a20"/></svg></div>
    <h3>NETWORK SECURITY</h3><p>Lorem ipsum dolor sit amet, consectetur adipisicing elit</p>
  </div>
</section>

<section class="solutions" role="img" aria-label="Dim office interior in the background">
  <h2 class="section-title">flexible solutions for your business needs</h2>
  <p class="intro"><em>(Kavnex) Key Assets Via Network Expertise</em> is a technology solution provider based in Riverton, Nevada. Our goal is to make technology a non-issue for individuals and small to medium size businesses ranging from 5 to 150 Users. Kavnex has the experience, the tools, high-level technology solutions and training to power your business and your work force. We understand that all business's have one goal in common!</p>

  <div class="card" style="left:65px;top:259px">
    <svg class="art" viewBox="0 0 68 68" style="border-radius:0"><circle cx="34" cy="34" r="30" fill="#3ecfa8"/><path d="M34 34L34 4A30 30 0 0 1 62 44z" fill="#f5c842"/><circle cx="34" cy="34" r="13" fill="#fff"/></svg>
    <h4>Managed IT Solutions</h4>
    <p>Our staff will design, service, administer and maintain your IT needs. We are well versed on all major operating system, and network appliances.</p>
  </div>
  <div class="card" style="left:432px;top:259px">
    <div class="art" role="img" aria-label="Orange stopwatch icon" style="background:#f39c12"></div>
    <h4 class="mid">Remote Diagnostic and Support</h4>
    <p>Do you need a quick solution to a technical problem? With our live remote-assistance tool, a member of our support team can view your desktop and share control of your mouse and keyboard to get you on your way to a solution.</p>
  </div>
  <div class="card" style="left:798px;top:259px">
    <div class="art" role="img" aria-label="Wrench and gear icon" style="background:#b9b3a6"></div>
    <h4>IT Infrastructure Design and Installation</h4>
    <p style="top:128px">Do you have more than one site? Do you need remote access? We can design and implement LANS/WANS and VPN's. Make your important data available to you wherever you are.</p>
  </div>
  <div class="card short" style="left:65px;top:623px">
    <div class="art" role="img" aria-label="Light bulb icon" style="background:#f2c81e"></div>
    <h4>SEO Marketing</h4>
    <p>Lorem ipsum dolor sit ame consectetur adipisicing elit</p>
  </div>
  <div class="card short" style="left:432px;top:623px">
    <div class="art" role="img" aria-label="Tablet in hand icon" style="background:#3a7fc1"></div>
    <h4>SEO Marketing</h4>
    <p>Lorem ipsum dolor sit ame consectetur adipisicing elit</p>
  </div>
  <div class="card short" style="left:798px;top:623px">
    <div class="art" role="img" aria-label="Lifebuoy icon" style="background:#e04a3a"></div>
    <h4>SEO Marketing</h4>
    <p>Lorem ipsum dolor sit ame consectetur adipisicing elit</p>
  </div>
</section>

<section class="contact">
  <div class="qc">
    <div class="col-title">Quick Contact</div>
    <div class="field" style="margin-top:40px">Name</div>
    <div class="field">E-mail Address</div>
    <div class="field area">Message</div>
    <span class="btn">Send Message</span>
  </div>
  <div class="why">
    <div class="col-title">Why our Clients Like Us</div>
    <p>Our clients choose Kavnex and stay with us because we deliver on every technology need they have. We have a 90% client retention rate. Many of our clients span ten or more years. Whether you need to completely outsource your IT requirements or add advanced insight to your existing IT department, Kavnex can serve as your complete outsourcing or as a compliment to your IT staff.</p>
  </div>
</section>

<section class="tabs">
  <div class="tab-list">
    <div>Responsive Web Design</div>
    <div class="on">Premium Plugin Included</div>
    <div>Predefine Layout</div>
    <div>Our Philosopy</div>
    <div>What We Do?</div>
  </div>
  <div class="tab-photo" role="img" aria-label="Photo of a smiling group of colleagues"></div>
  <div class="tab-body">
    <h5>Adipisicing elit</h5>
    <p>There are many variations of passages of Lorem Ipsum available, but the majority have suffered alteration in some form, by injected humour, or randomised words which don't look even slightly believable. If you are going to use.</p>
  </div>
</section>

<aside class="testimonials">
  <h6>Testimonials</h6>
  <div class="quote">Lorem ipsum dolor sit amet, consectetur adipisicing elit, sed do eiusmod tempor incididunt<b>-John Doe/ <span style="font-weight:400">Director of samplecorp.com</span></b></div>
  <div class="quote">Lorem ipsum dolor sit amet, consectetur adipisicing elit, sed do eiusmod tempor incididunt<b>-John Doe/ <span style="font-weight:400">Director of samplecorp.com</span></b></div>
</aside>

<footer class="footer">
  <div class="fcol" style="left:65px"><h6>CONTACT US</h6><p>Phone: 12345678<br>Email: xxxxx@mailbox.com<br>Fax: xxxxxxxxxxx</p></div>
  <div class="fcol" style="left:339px"><h6>ADDRESS</h6><p style="line-height:22px">abcd/2 abc Road, city, state, country,<br>11212121</p></div>
  <div class="fcol" style="left:614px"><h6>NEWSLETTER</h6><div class="news-field">E-mail Address</div><span class="btn">Join</span></div>
  <div class="fcol" style="left:890px"><h6>SOCIAL LINKS</h6><div class="social-foot"><span></span><span></span><span></span><span></span><span></span></div></div>
</footer>
<div class="rule"></div>
<div class="bottom">
  <div class="copy">Copyright © 2007 - Kavnex Development Group, Inc - All rights reserved</div>
  <div class="links"><span>Home</span><span>About Us</span><span>Testimonial</span><span>Contact Us</span></div>
</div>

</body>
</html>
```